Harlow Reese, LLC Website

We are a small law firm in need of a website that contains the following:
1. Attractive main page
2. About us/attorney info for three people: Martin Harlow (attorney), Dean Reese (attorney), and Melissa Durant (legal assistant). We have bio's ready to submit.
3. Blog/video page. We'd like to post blogs and videos to help drive traffic
4. Multidistrict Litigation and Class Actions page, where we post information regarding active MDLs and Class actions that we are doing intake on.
Updates

Can you also please use the color "gold" in the design and logo? Thanks.

Industry/Entity Type

Legal

Coding

Coded - Design and coding required

Number of Pages Required

1 page

Colors
0054AA
0677BA
7BADD7
CADEEF
E8F1F8

Requirements
Must have
• 1. Attractive main page 2. About us/attorney info for three people: Martin Harlow (attorney), Dean Reese (attorney), and Melissa Durant (legal assistant). We have bio's ready to submit. 3. Blog/video page. We'd like to post blogs and videos to help drive traffic 4. Multidistrict Litigation and Class Actions page, where we post information regarding active MDLs and Class actions that we are doing intake on.

```html
<!DOCTYPE html>
<html lang="en">
<head>
<meta charset="utf-8">
<title>Harlow Reese, LLC — Lawyers</title>
<link href="https://fonts.googleapis.com/css2?family=Poppins:wght@400;500;600;700&display=swap" rel="stylesheet">
<style>
:root{
  --navy:#2b3585;
  --navy-dark:#1f2868;
  --sky:#4aaee3;
  --gold:#c9a04a;
  --gold-light:#e3c67f;
  --sky-light:#e8f1f8;
  --pale:#f2f4fb;
  --text:#4a4f63;
  --white:#ffffff;
  --line:#d8dcea;
}
*{box-sizing:border-box;margin:0;padding:0}
html,body{width:1200px;height:4286px;overflow:hidden}
body{font-family:'Poppins',sans-serif;color:var(--text);background:var(--white);position:relative}
.abs{position:absolute}
.brand{display:flex;align-items:center;border:2px solid var(--navy);height:48px;background:var(--white)}
.brand-mark{width:60px;height:100%;background:var(--navy);display:flex;align-items:center;justify-content:center}
.brand-mark i{display:block;width:18px;height:18px;background:var(--gold)}
.brand-name{padding:0 14px;font-weight:600;font-size:20px;color:var(--sky);letter-spacing:.2px}
/* header */
.site-header{left:0;top:0;width:1200px;height:92px;background:var(--white)}
.site-header .brand{left:93px;top:22px}
.main-nav{left:412px;top:36px;display:flex;gap:40px;font-size:13px;font-weight:500;color:var(--navy)}
.phone-btn{left:914px;top:22px;width:190px;height:46px;border:2px solid var(--navy);display:flex;align-items:center}
.phone-btn .ico{width:48px;height:100%;background:var(--navy);display:flex;align-items:center;justify-content:center}
.phone-btn span{padding-left:14px;font-weight:600;font-size:14px;color:var(--navy)}
/* hero */
.hero{left:0;top:92px;width:1200px;height:644px;background:linear-gradient(100deg,#2c3242 0%,#434a5c 38%,#6a5c44 55%,#3a4256 75%,#1f2d52 100%)}
.hero-eyebrow{left:93px;top:146px;font-size:23px;font-weight:500;color:var(--white)}
.hero-title{left:93px;top:176px;font-size:45px;font-weight:700;line-height:53px;color:var(--white)}
.hero-sub{left:93px;top:298px;font-size:16px;color:#e6e8ef}
.consult-btn{left:93px;top:356px;height:52px;width:235px;border:2px solid var(--white);display:flex;align-items:center}
.consult-btn .ico{width:70px;height:100%;background:var(--white);display:flex;align-items:center;justify-content:center}
.consult-btn span{padding-left:20px;font-size:15px;font-weight:700;color:var(--white)}
.scroll-down{left:1142px;top:196px;width:16px;height:220px}
.scroll-down .rail{position:absolute;left:7px;top:0;width:1px;height:100px;background:rgba(255,255,255,.6)}
.scroll-down .label{position:absolute;left:-34px;top:150px;transform:rotate(-90deg);font-size:11px;color:var(--white);white-space:nowrap;letter-spacing:.5px}
/* section tag & heading */
.tag{display:flex;align-items:center;height:44px;border:2px solid var(--navy);background:var(--white)}
.tag .mark{width:60px;height:100%;background:var(--navy);display:flex;align-items:center;justify-content:center}
.tag .mark i{display:block;width:16px;height:16px;background:var(--gold)}
.tag span{padding:0 16px;font-size:14px;font-weight:600;color:var(--navy)}
.sec-title{font-size:36px;font-weight:600;color:var(--navy);text-align:center;width:1200px;left:0;line-height:44px}
.sec-lead{width:1200px;left:0;text-align:center;font-size:16px;line-height:28px}
/* about */
.about{left:0;top:736px;width:1200px;height:824px;background:var(--white)}
.team-card{width:326px;height:367px;top:362px}
.team-frame{position:absolute;left:0;top:0;width:326px;height:305px;border:3px solid var(--navy);background:var(--pale)}
.team-photo{position:absolute;left:60px;top:-16px;width:206px;height:300px;background:linear-gradient(180deg,#c9cedd,#2d3347 60%,#1d2233)}
.team-label{position:absolute;left:26px;top:270px;width:275px;height:97px;background:var(--white);box-shadow:0 8px 24px rgba(40,50,100,.12);text-align:center;padding-top:18px;border-bottom:3px solid var(--gold)}
.team-label h3{font-size:19px;font-weight:600;color:var(--navy)}
.team-label p{font-size:16px;color:var(--text)}
.team-label.active{top:186px;height:181px;background:var(--sky);padding-top:20px}
.team-label.active h3,.team-label.active p{color:var(--white)}
.team-label.active .bio{font-size:14px;line-height:28px;margin-top:10px}
.team-label .more{position:absolute;left:119px;bottom:-14px;width:36px;height:34px;background:var(--navy);display:flex;align-items:center;justify-content:center}
/* blog */
.blog{left:0;top:1560px;width:1200px;height:937px;background:var(--pale)}
.post{width:325px;top:340px}
.post-img{position:relative;width:325px;height:240px}
.date-chip{position:absolute;left:5px;top:24px;background:var(--sky);color:var(--white);font-size:10px;font-weight:600;padding:2px 6px}
.play{position:absolute;left:137px;top:95px;width:50px;height:50px;border-radius:50%;background:var(--white);display:flex;align-items:center;justify-content:center}
.post .author{margin-top:30px;font-size:11px;font-weight:600;color:var(--navy)}
.post .author::before{content:"";display:inline-block;width:4px;height:4px;border-radius:50%;background:var(--gold);margin-right:6px;vertical-align:middle}
.post h3{margin-top:16px;font-size:18px;line-height:28px;font-weight:600;color:var(--navy)}
.post p{margin-top:10px;font-size:16px;line-height:28px}
.read-btn{display:flex;align-items:center;height:46px;width:204px;border:2px solid var(--navy);background:var(--white)}
.read-btn .ico{width:70px;height:100%;background:var(--navy);display:flex;align-items:center;justify-content:center}
.read-btn span{padding-left:20px;font-size:15px;font-weight:700;color:var(--navy)}
.post .read-btn{margin-top:28px}
/* mdl */
.mdl{left:0;top:2497px;width:1200px;height:670px;background:var(--white)}
.mdl-title{left:93px;top:174px;font-size:36px;line-height:44px;font-weight:600;color:var(--navy);white-space:nowrap}
.mdl-copy{left:93px;top:272px;width:505px;font-size:16px;line-height:27.5px}
.mdl-copy p+p{margin-top:27px}
.mdl-frame{left:659px;top:140px;width:445px;height:393px;border:3px solid var(--navy)}
.mdl-photo{left:659px;top:157px;width:428px;height:359px;background:linear-gradient(135deg,#dfe3ec,#9aa2b4 45%,#39415a 75%,#2a3148)}
/* contact */
.contact{left:0;top:3167px;width:1200px;height:627px;background:linear-gradient(160deg,#6f86a0 0%,#c8ad7d 40%,#8e7650 70%,#3d3a36 100%)}
.contact svg.band{position:absolute;left:0;top:0}
.contact-title{left:626px;top:152px;font-size:36px;line-height:44px;font-weight:600;color:var(--navy)}
.field{height:52px;background:var(--white);display:flex;align-items:center;padding-left:18px;font-size:14px;color:#6a6f80;gap:12px}
.field.area{align-items:flex-start;padding-top:20px}
.send-btn{left:626px;top:497px;height:52px;width:234px;border:2px solid var(--navy);display:flex;align-items:center;background:var(--sky)}
.send-btn .ico{width:70px;height:100%;background:var(--navy);display:flex;align-items:center;justify-content:center}
.send-btn span{padding-left:20px;font-size:15px;font-weight:700;color:var(--navy)}
/* footer */
.site-footer{left:0;top:3794px;width:1200px;height:492px;background:var(--white)}
.site-footer .brand{left:93px;top:101px}
.foot-about{left:93px;top:178px;width:360px;font-size:16px;line-height:28px}
.vline{width:2px;height:250px;top:84px;background:linear-gradient(180deg,var(--sky),rgba(74,174,227,0))}
.foot-h{font-size:14px;font-weight:600;color:var(--navy)}
.foot-links{list-style:none;font-size:16px;line-height:38px;color:var(--text)}
.info-row{display:flex;align-items:flex-start;gap:20px;font-size:16px;line-height:27px;color:var(--text)}
.info-row .dot{flex:none;width:38px;height:38px;border-radius:50%;background:var(--sky);display:flex;align-items:center;justify-content:center}
.bottom-line{left:0;top:398px;width:1200px;height:1px;background:var(--line)}
.copyright{left:93px;top:435px;font-size:13px;font-weight:500;color:var(--navy)}
.socials{left:924px;top:425px;display:flex;gap:9px}
.socials span{width:38px;height:38px;border-radius:50%;background:var(--navy);display:block}
</style>
</head>
<body>

<header class="site-header abs">
  <div class="brand abs"><div class="brand-mark"><i></i></div><div class="brand-name">HARLOW REESE LLC</div></div>
  <nav class="main-nav abs"><span>HOME</span><span>ATTORNEY</span><span>BLOG</span><span>MULTIDISTRICT LITIGATION</span></nav>
  <div class="phone-btn abs">
    <div class="ico"><svg width="16" height="16" viewBox="0 0 24 24"><path fill="#fff" d="M6.6 10.8a15 15 0 0 0 6.6 6.6l2.2-2.2a1 1 0 0 1 1-.25 11.4 11.4 0 0 0 3.6.57 1 1 0 0 1 1 1V20a1 1 0 0 1-1 1A17 17 0 0 1 3 4a1 1 0 0 1 1-1h3.5a1 1 0 0 1 1 1c0 1.25.2 2.45.57 3.57a1 1 0 0 1-.25 1z"/></svg></div>
    <span>(555) 014-2730</span>
  </div>
</header>

<section class="hero abs" role="img" aria-label="Photo of a lawyer at a desk with a judge's gavel and pen">
  <div class="hero-eyebrow abs">WE WOULD BE HONORED TO</div>
  <h1 class="hero-title abs">PROVIDE YOU WITH<br>A LEGAL CONSULTATION.</h1>
  <p class="hero-sub abs">Inventore veritatis et quasi architecto beatae vitae dicta sunt.</p>
  <div class="consult-btn abs">
    <div class="ico"><svg width="26" height="16" viewBox="0 0 26 16"><path d="M2 4h6l5 4 5-4h6v8h-5l-6 3-6-3H2z" fill="none" stroke="#4aaee3" stroke-width="2" stroke-linejoin="round"/></svg></div>
    <span>CONSULT NOW</span>
  </div>
  <div class="scroll-down abs"><div class="rail"></div><div class="label">‹ SCROLL DOWN</div></div>
</section>

<section class="about abs">
  <div class="tag abs" style="left:484px;top:104px"><div class="mark"><i></i></div><span>ABOUT LAWYER</span></div>
  <h2 class="sec-title abs" style="top:158px">MEET OUR ATTORNEY</h2>
  <p class="sec-lead abs" style="top:216px">Ut enim ad minim veniam quis nostrud exercitation ullamco laboris nisi ut aliost<br>uip ex ea commodo consequat. Duis aute irure dolor in reprehenderit in volu<br>cillum dolore eu fugiat nulla pariaturse.</p>

  <article class="team-card abs" style="left:93px">
    <div class="team-frame"></div>
    <div class="team-photo" role="img" aria-label="Portrait of attorney Martin Harlow in a dark suit"></div>
    <div class="team-label"><h3>MARTIN HARLOW</h3><p>Attorney</p></div>
  </article>
  <article class="team-card abs" style="left:437px">
    <div class="team-frame"></div>
    <div class="team-photo" role="img" aria-label="Portrait of attorney Dean Reese in a grey suit"></div>
    <div class="team-label active"><h3>DEAN REESE</h3><p>Attorney</p><p class="bio">Incididunt ut labore et sed<br>dolore magna aliqua.</p>
      <div class="more"><svg width="10" height="12" viewBox="0 0 10 12"><path d="M3 2l4 4-4 4" fill="none" stroke="#fff" stroke-width="2"/></svg></div></div>
  </article>
  <article class="team-card abs" style="left:780px">
    <div class="team-frame"></div>
    <div class="team-photo" role="img" aria-label="Portrait of legal assistant Melissa Durant"></div>
    <div class="team-label"><h3>MELISSA DURANT</h3><p>Legal Assistant</p></div>
  </article>
</section>

<section class="blog abs">
  <div class="tag abs" style="left:520px;top:129px"><div class="mark"><i></i></div><span>LATEST BLOG</span></div>
  <h2 class="sec-title abs" style="top:183px">RECENT BLOG POST</h2>
  <p class="sec-lead abs" style="top:241px">Ut enim ad minim veniam quis nostrud exercitation ullamco laboris nisi ut aliost<br>uip ex ea commodo consequat uis aute irure dolor in reprehenderit</p>

  <article class="post abs" style="left:93px">
    <div class="post-img" role="img" aria-label="Lawyer signing papers beside brass scales of justice" style="background:linear-gradient(135deg,#2a2f3c,#6b5a3e 55%,#1c1f27)"><span class="date-chip">05 APR, 2025</span></div>
    <div class="author">OWEN PRATT</div>
    <h3>UT ENIM AD MINIMA VENIAMO<br>CUIS NOSTRUM EXERCUL.</h3>
    <p>Allamco laboris nisi ut aliost uiex<br>commodo consequat aute.</p>
    <div class="read-btn"><div class="ico"><svg width="10" height="12" viewBox="0 0 10 12"><path d="M3 2l4 4-4 4" fill="none" stroke="#4aaee3" stroke-width="2"/></svg></div><span>READ MORE</span></div>
  </article>
  <article class="post abs" style="left:437px">
    <div class="post-img" role="img" aria-label="Video still of two lawyers reviewing a document" style="background:linear-gradient(135deg,#a7abb3,#4d525e 50%,#23262e)"><span class="date-chip">05 APR, 2025</span>
      <div class="play"><svg width="16" height="18" viewBox="0 0 16 18"><path d="M3 2l11 7-11 7z" fill="#4aaee3"/></svg></div></div>
    <div class="author">OWEN PRATT</div>
    <h3>UT ENIM AD MINIMA VENIAMO<br>CUIS NOSTRUM EXERCUL.</h3>
    <p>Allamco laboris nisi ut aliost uiex<br>commodo consequat aute.</p>
    <div class="read-btn"><div class="ico"><svg width="10" height="12" viewBox="0 0 10 12"><path d="M3 2l4 4-4 4" fill="none" stroke="#4aaee3" stroke-width="2"/></svg></div><span>READ MORE</span></div>
  </article>
  <article class="post abs" style="left:780px">
    <div class="post-img" role="img" aria-label="Business people meeting in a bright office" style="background:linear-gradient(135deg,#e4e6ea,#9ea4b0 45%,#2c3345)"><span class="date-chip">05 APR, 2025</span></div>
    <div class="author">OWEN PRATT</div>
    <h3>UT ENIM AD MINIMA VENIAMO<br>CUIS NOSTRUM EXERCUL.</h3>
    <p>Allamco laboris nisi ut aliost uiex<br>commodo consequat aute.</p>
    <div class="read-btn"><div class="ico"><svg width="10" height="12" viewBox="0 0 10 12"><path d="M3 2l4 4-4 4" fill="none" stroke="#4aaee3" stroke-width="2"/></svg></div><span>READ MORE</span></div>
  </article>
</section>

<section class="mdl abs">
  <div class="tag abs" style="left:93px;top:106px"><div class="mark"><i></i></div><span>CLASS ACTIONS</span></div>
  <h2 class="mdl-title abs">MULTIDISTRICT LITIGATION<br>AND CLASS ACTIONS</h2>
  <div class="mdl-copy abs">
    <p>Duis aute irure dolor in reprehenderit in voluptate velit esse cillum dolore eu fugiat nulla pariatur. Excepteur sint occaecat cupidatat non proident sunt in culpa qui officia deserunt mollit anim id est laborum.</p>
    <p>Excepteur sint occaecat cupidatat non proident, sunt in culpa qui officia deserunt mollit anim id est laborum. Sed ut perspiciatis unde omnis iste natus error sit</p>
  </div>
  <div class="read-btn abs" style="left:93px;top:516px"><div class="ico"><svg width="10" height="12" viewBox="0 0 10 12"><path d="M3 2l4 4-4 4" fill="none" stroke="#4aaee3" stroke-width="2"/></svg></div><span>READ MORE</span></div>
  <div class="mdl-frame abs"></div>
  <div class="mdl-photo abs" role="img" aria-label="Three lawyers discussing documents at a table"></div>
  <div class="abs" style="left:820px;top:137px;width:3px;height:16px;background:var(--gold)"></div>
  <div class="abs" style="left:820px;top:516px;width:3px;height:20px;background:var(--gold)"></div>
  <div class="abs" style="left:1030px;top:528px;width:30px;height:8px;background:var(--white)"></div>
</section>

<section class="contact abs">
  <div class="abs" role="img" aria-label="Looking up at tall stone courthouse columns" style="left:0;top:0;width:600px;height:627px"></div>
  <svg class="band" width="1200" height="627" viewBox="0 0 1200 627">
    <polygon points="433,0 1200,0 1200,627 433,627 574,286" fill="#4aaee3"/>
    <polyline points="420,0 561,286 420,627" fill="none" stroke="#ffffff" stroke-width="4"/>
  </svg>
  <div class="tag abs" style="left:626px;top:78px"><div class="mark"><i></i></div><span>CONTACT US</span></div>
  <h2 class="contact-title abs">REQUEST A QUOTE &amp;<br>CONSULTATION</h2>
  <div class="field abs" style="left:626px;top:246px;width:234px"><svg width="12" height="12" viewBox="0 0 12 12"><circle cx="6" cy="3.5" r="2.5" fill="#9aa0b0"/><path d="M1 12a5 5 0 0 1 10 0z" fill="#9aa0b0"/></svg>Full Name</div>
  <div class="field abs" style="left:871px;top:246px;width:234px"><svg width="13" height="10" viewBox="0 0 13 10"><rect width="13" height="10" fill="#9aa0b0"/><path d="M0 0l6.5 5L13 0" fill="none" stroke="#fff"/></svg>Email Address</div>
  <div class="field abs" style="left:626px;top:311px;width:234px"><svg width="12" height="12" viewBox="0 0 24 24"><path fill="#9aa0b0" d="M6.6 10.8a15 15 0 0 0 6.6 6.6l2.2-2.2a1 1 0 0 1 1-.25 11.4 11.4 0 0 0 3.6.57 1 1 0 0 1 1 1V20a1 1 0 0 1-1 1A17 17 0 0 1 3 4a1 1 0 0 1 1-1h3.5a1 1 0 0 1 1 1c0 1.25.2 2.45.57 3.57a1 1 0 0 1-.25 1z"/></svg>Phone Number</div>
  <div class="field abs" style="left:871px;top:311px;width:234px"><svg width="12" height="12" viewBox="0 0 12 12"><rect x="5" y="0" width="7" height="4" fill="#9aa0b0" transform="rotate(45 8 2)"/><path d="M1 11l5-5" stroke="#9aa0b0" stroke-width="2"/></svg>Case Type<svg style="margin-left:auto;margin-right:18px" width="10" height="6" viewBox="0 0 10 6"><path d="M1 1l4 4 4-4" fill="none" stroke="#2b3585" stroke-width="1.6"/></svg></div>
  <div class="field area abs" style="left:626px;top:377px;width:479px;height:109px"><svg width="12" height="12" viewBox="0 0 12 12"><path d="M0 0h12v8H4l-3 3V8H0z" fill="#9aa0b0"/></svg>Leave your message...</div>
  <div class="send-btn abs"><div class="ico"><svg width="10" height="12" viewBox="0 0 10 12"><path d="M3 2l4 4-4 4" fill="none" stroke="#4aaee3" stroke-width="2"/></svg></div><span>SEND MESSAGE</span></div>
</section>

<footer class="site-footer abs">
  <div class="brand abs"><div class="brand-mark"><i></i></div><div class="brand-name">HARLOW REESE LLC</div></div>
  <p class="foot-about abs">Duis aute irure dolor in reprehendrit intui volupt ate velit esse cillum dolore eufu giat nulla pariatur excepteur.</p>
  <div class="vline abs" style="left:497px"></div>
  <div class="abs" style="left:563px;top:100px">
    <div class="foot-h">NAVIGATION</div>
    <ul class="foot-links" style="margin-top:6px"><li>Home</li><li>Attorney</li><li>Blog</li><li>Multidistrict Litigation</li></ul>
  </div>
  <div class="vline abs" style="left:805px"></div>
  <div class="abs" style="left:870px;top:100px">
    <div class="foot-h">CONTACT INFORMATION</div>
    <div class="info-row" style="margin-top:18px"><div class="dot"><svg width="12" height="16" viewBox="0 0 12 16"><path d="M6 0a6 6 0 0 1 6 6c0 4-6 10-6 10S0 10 0 6a6 6 0 0 1 6-6z" fill="#fff"/></svg></div><div>214 Linden Ave. Fairview,<br>AL 36500</div></div>
    <div class="info-row" style="margin-top:10px;align-items:center"><div class="dot"><svg width="14" height="14" viewBox="0 0 24 24"><path fill="#fff" d="M6.6 10.8a15 15 0 0 0 6.6 6.6l2.2-2.2a1 1 0 0 1 1-.25 11.4 11.4 0 0 0 3.6.57 1 1 0 0 1 1 1V20a1 1 0 0 1-1 1A17 17 0 0 1 3 4a1 1 0 0 1 1-1h3.5a1 1 0 0 1 1 1c0 1.25.2 2.45.57 3.57a1 1 0 0 1-.25 1z"/></svg></div><div>(555) 014-2730</div></div>
    <div class="info-row" style="margin-top:16px;align-items:center"><div class="dot"><svg width="14" height="14" viewBox="0 0 14 14"><rect x="2" y="5" width="10" height="8" fill="#fff"/><rect x="4" y="1" width="6" height="4" fill="none" stroke="#fff" stroke-width="1.5"/></svg></div><div>(555) 014-2731</div></div>
  </div>
  <div class="bottom-line abs"></div>
  <div class="copyright abs">COPYRIGHT © 2025 HARLOW REESE LLC. ALL RIGHTS RESERVED.</div>
  <div class="socials abs"><span></span><span></span><span></span><span></span></div>
</footer>

</body>
</html>
```